42 on Birch Apartment Mailer to Competition

I need a postcard mailer designed that will be promoting a new apartment building in downtown Rochester NY. The postcards are being mailed to other apartment communities the we are in direct competition with. I have enclosed a bunch of info to guide you.

Target Market(s)

Other communities in the market

Industry/Entity Type

Property Management

Requirements
Must have
• Exterior rendering, features. Fit standard postcard, colors similar to enclosed, grey, white coral
Nice to have
• Interior Pictures

```html
<!DOCTYPE html>
<html lang="en">
<head>
<meta charset="utf-8">
<title>42 on Birch Postcard Mailer</title>
<link rel="stylesheet" href="https://fonts.googleapis.com/css2?family=Fira+Sans+Condensed:wght@400;700&display=swap">
<style>
  :root {
    --backdrop: #fbe6e3;
    --white: #ffffff;
    --maroon: #5c1c1a;
    --maroon-deep: #7a1f1d;
    --coral: #d6532f;
    --red: #e0342a;
    --ink: #2b2b2b;
  }
  html, body {
    margin: 0;
    padding: 0;
    width: 1200px;
    height: 1035px;
    overflow: hidden;
    background: var(--backdrop);
    font-family: "Fira Sans Condensed", "Arial Narrow", sans-serif;
  }
  .postcard {
    position: absolute;
    border-radius: 12px;
    overflow: hidden;
    background: var(--white);
    box-shadow: 0 6px 18px rgba(90, 30, 30, 0.18);
  }
  .postcard-art { position: absolute; inset: 0; }

  /* Front side */
  .postcard-front { left: 30px; top: 92px; width: 560px; height: 850px; }
  .front-brand {
    position: absolute;
    left: 20px;
    top: 150px;
    display: flex;
    align-items: center;
    gap: 8px;
    color: var(--maroon-deep);
    font-weight: 700;
    font-size: 24px;
    line-height: 30px;
    text-transform: uppercase;
    white-space: nowrap;
  }
  .brand-mark { width: 16px; height: 16px; background: var(--maroon-deep); flex: none; }
  .panel { position: absolute; color: var(--white); }
  .panel h2 {
    margin: 0 0 6px;
    font-size: 20px;
    line-height: 22px;
    font-weight: 700;
    text-transform: uppercase;
  }
  .panel ul { list-style: none; margin: 0; padding: 0; font-size: 14px; line-height: 18px; }
  .floor-plans { left: 20px; top: 292px; width: 240px; }
  .community-features { left: 10px; top: 560px; width: 270px; text-align: center; }
  .community-features ul { font-size: 14px; line-height: 17px; }
  .home-features { left: 305px; top: 422px; width: 245px; }
  .home-features ul { font-size: 14.5px; line-height: 19px; }
  .contact-strip {
    position: absolute;
    left: 0;
    right: 0;
    top: 798px;
    height: 52px;
    display: flex;
    align-items: center;
    justify-content: center;
    gap: 12px;
    color: var(--ink);
    font-size: 16px;
    letter-spacing: 0.2px;
  }
  .divider { font-weight: 700; }

  /* Back side */
  .postcard-back { left: 615px; top: 368px; width: 560px; height: 300px; }
  .back-brand {
    position: absolute;
    left: 14px;
    top: 28px;
    display: flex;
    align-items: center;
    gap: 6px;
    color: var(--maroon-deep);
    font-weight: 700;
    font-size: 18px;
    line-height: 26px;
    text-transform: uppercase;
    white-space: nowrap;
  }
  .back-brand .brand-mark { width: 12px; height: 12px; }
  .call-to-action {
    position: absolute;
    left: 14px;
    top: 176px;
    width: 230px;
    color: var(--white);
  }
  .call-to-action h2 {
    margin: 0;
    font-size: 19px;
    line-height: 20px;
    font-weight: 700;
    text-transform: uppercase;
  }
  .call-phone {
    margin: 2px 0 0;
    color: var(--red);
    font-size: 26px;
    line-height: 28px;
    font-weight: 700;
  }
  .call-line { margin: 0; font-size: 12px; line-height: 14px; text-transform: uppercase; }
  .call-follow { margin: 2px 0 0; font-size: 11px; line-height: 13px; }
</style>
</head>
<body>
  <article class="postcard postcard-front">
    <svg class="postcard-art" width="560" height="850" viewBox="0 0 560 850">
      <defs>
        <linearGradient id="renderingTone" x1="0" y1="0" x2="1" y2="1">
          <stop offset="0" stop-color="#c9d1d6"/>
          <stop offset="0.45" stop-color="#9eaab2"/>
          <stop offset="0.75" stop-color="#b9a79c"/>
          <stop offset="1" stop-color="#6f7a62"/>
        </linearGradient>
        <clipPath id="belowCurve">
          <path d="M0,560 C170,450 360,350 560,320 L560,798 L0,798 Z"/>
        </clipPath>
        <clipPath id="aboveCurve">
          <path d="M0,0 L560,0 L560,320 C360,350 170,450 0,560 Z"/>
        </clipPath>
      </defs>

      <rect class="exterior-rendering" x="0" y="0" width="560" height="600" fill="url(#renderingTone)" role="img" aria-label="Exterior rendering of the glass apartment tower at dusk"/>

      <g clip-path="url(#aboveCurve)">
        <rect class="floor-plans-band" x="0" y="282" width="290" height="300" fill="var(--coral)" opacity="0.88"/>
      </g>

      <g clip-path="url(#belowCurve)">
        <rect class="community-band" x="0" y="300" width="290" height="500" fill="var(--maroon)" opacity="0.96"/>
        <rect class="home-band" x="290" y="300" width="270" height="500" fill="var(--coral)" opacity="0.94"/>
      </g>

      <path class="curve-rule" d="M0,560 C170,450 360,350 560,320" fill="none" stroke="var(--white)" stroke-width="5"/>

      <circle class="brand-disc" cx="75" cy="165" r="112" fill="var(--white)" stroke="var(--maroon-deep)" stroke-width="4"/>

      <rect class="contact-band" x="0" y="798" width="560" height="52" fill="var(--white)"/>
      <path class="contact-tab" d="M0,798 L24,798 L0,834 Z" fill="var(--maroon)"/>
      <path class="contact-ribbon" d="M515,798 L560,798 L560,824 Z" fill="var(--coral)"/>
    </svg>

    <div class="front-brand"><span class="brand-mark"></span>42 on Birch</div>

    <section class="panel floor-plans">
      <h2>Floor Plans</h2>
      <ul>
        <li>1 Bedroom</li>
        <li>1 Bedroom with Den</li>
        <li>1 and 2 Bedroom 2 Bath Available</li>
        <li>$1400 to $3300</li>
        <li>775 to 1677 sq. ft.</li>
      </ul>
    </section>

    <section class="panel community-features">
      <h2>Community Features</h2>
      <ul>
        <li>Rooftop patio</li>
        <li>24 Hour Fitness</li>
        <li>5x10 Storage Unit</li>
        <li>High Speed Internet and cable Included</li>
        <li>Heat and A/C Included</li>
        <li>Parking Available, One Spot Included</li>
        <li>Modern Security with Controlled Access<br>and Key Fobs</li>
        <li>Amazing Views</li>
        <li>Den Available</li>
        <li>24 Hour Maintenance</li>
      </ul>
    </section>

    <section class="panel home-features">
      <h2>Home Features</h2>
      <ul>
        <li>Floor to Ceiling Operable Windows</li>
        <li>W/D In Unit</li>
        <li>LED Lighting</li>
        <li>Hardwood Flooring</li>
        <li>Automatic Window Treatments</li>
        <li>Granite Countertops</li>
        <li>Undermount Sinks</li>
        <li>Tile backsplash</li>
        <li>Walk-In Closets Available</li>
        <li>Open Floor Plans</li>
        <li>Contemporary Cabinetry and Fixtures</li>
      </ul>
    </section>

    <footer class="contact-strip">
      <span>585.555.0142</span>
      <span class="divider">|</span>
      <span>LEASING@42ONBIRCH.COM</span>
      <span class="divider">|</span>
      <span>WWW.42ONBIRCH.COM</span>
    </footer>
  </article>

  <article class="postcard postcard-back">
    <svg class="postcard-art" width="560" height="300" viewBox="0 0 560 300">
      <path class="back-panel" d="M0,0 L255,0 C282,80 282,220 255,300 L0,300 Z" fill="var(--maroon)"/>
      <path class="back-panel-edge" d="M255,0 C282,80 282,220 255,300" fill="none" stroke="var(--red)" stroke-width="4"/>
      <path class="back-brand-tab" d="M0,16 L150,16 A27,27 0 0 1 150,70 L0,70 Z" fill="var(--white)" stroke="var(--red)" stroke-width="3"/>
      <rect class="interior-kitchen" x="8" y="82" width="120" height="84" fill="#8a7c72" role="img" aria-label="Interior photo of the kitchen with island and stools"/>
      <rect class="interior-living" x="134" y="82" width="122" height="84" fill="#6d5a4a" role="img" aria-label="Interior photo of the living area"/>
      <rect class="back-rule" x="0" y="168" width="266" height="3" fill="var(--red)"/>
    </svg>

    <div class="back-brand"><span class="brand-mark"></span>42 on Birch</div>

    <section class="call-to-action">
      <h2>Call Today<br>For Information</h2>
      <p class="call-phone">585.555.0142</p>
      <p class="call-line">LEASING@42ONBIRCH.COM</p>
      <p class="call-line">WWW.42ONBIRCH.COM</p>
      <p class="call-follow">Follow us on our social pages</p>
    </section>
  </article>
</body>
</html>
```